Rory Vandermeer | Inbound Marketing

Need a logo for a company that fills the need of creating a consistent stream of warm sales leads and revenue (via building of a sales funnel) to companies who either do not have sales teams or use outmoded outbound sales strategy to address the company bottom line. This includes Inbound marketing, SEO, content marketing strategy

Target Market(s)

Small to Medium Size Businesses, who are willing to spend thousands or tens of thousands of dollars on avertising.

Industry/Entity Type

It Company

Contact Information for Business Card

Content Strategy | PPC | SEO | Local Social & SEO
512.604.7193
roryvandermeer@quillmail.net

Logo Text

Look Inward to Gain Outward

Font styles to use
Sans Serif

Requirements
Nice to have
• I am partial to funnels in natural phenomena (tornados, whirlpools, hurricanes, black holes, spiral galaxies) but this is not a deal breaker. In fact, I don't want to intimidate anybody and seeing photos and artist representation are somewhat unsettling to me as to their vastness and darkness

```html
<!DOCTYPE html>
<html lang="en">
<head>
<meta charset="utf-8">
<title>Rory Vandermeer | Inbound Marketing — Business Card</title>
<link rel="stylesheet" href="https://fonts.googleapis.com/css2?family=Questrial&display=swap">
<style>
  :root {
    --backdrop: #e4e3ef;
    --navy: #24527c;
    --paper: #f4f6f9;
    --slate: #8e9195;
    --rule: #9ea3a8;
    --ink-soft: #5e6368;
    --white: #ffffff;
  }
  * { box-sizing: border-box; margin: 0; padding: 0; }
  html, body {
    width: 1200px; height: 906px; overflow: hidden;
    background: var(--backdrop);
  }
  .canvas { position: relative; width: 1200px; height: 906px; }

  .card {
    position: absolute; width: 560px; height: 320px;
    box-shadow: 0 6px 18px rgba(40, 40, 80, 0.15);
  }
  .card--front { left: 80px; top: 110px; background: var(--navy); }
  .card--back  { left: 560px; top: 476px; background: var(--paper); overflow: hidden; }

  .name {
    position: absolute; text-align: right;
    font-family: "Questrial", "Century Gothic", sans-serif;
    font-weight: 400; font-size: 24px; line-height: 1.1;
    letter-spacing: 1.5px; text-transform: uppercase; white-space: nowrap;
  }
  .name__line { display: block; }

  .card--front .name { right: 290px; top: 122px; color: var(--white); }
  .card--front .divider {
    position: absolute; left: 284px; top: 112px; width: 1px; height: 76px;
    background: var(--rule);
  }
  .card--front .tagline {
    position: absolute; left: 298px; top: 128px;
    font-family: "Questrial", "Century Gothic", sans-serif;
    font-size: 13px; line-height: 1.2; letter-spacing: 1px;
    color: var(--slate); text-transform: uppercase;
  }

  .card--back .name { right: 300px; top: 84px; color: var(--navy); }
  .card--back .tagline {
    position: absolute; right: 300px; top: 142px;
    font-family: "Questrial", "Century Gothic", sans-serif;
    font-size: 12px; letter-spacing: 0.5px;
    color: var(--slate); text-transform: uppercase;
  }
  .card--back .divider {
    position: absolute; left: 280px; top: 72px; width: 1px; height: 92px;
    background: var(--rule);
  }
  .contact {
    position: absolute; left: 296px; top: 78px; list-style: none;
    font-family: "Questrial", "Century Gothic", sans-serif;
    font-size: 13px; color: var(--ink-soft);
  }
  .contact__item { display: flex; align-items: center; gap: 8px; height: 22px; }
  .contact__icon { width: 12px; height: 12px; flex: none; }

  .services {
    position: absolute; left: 0; right: 0; top: 238px; text-align: center;
    font-family: "Questrial", "Century Gothic", sans-serif;
    font-size: 14px; letter-spacing: 0.5px;
    color: var(--slate); text-transform: uppercase; word-spacing: 2px;
  }
  .services__sep { margin: 0 10px; }
  .band {
    position: absolute; left: 0; bottom: 0; width: 100%; height: 20px;
    background: var(--navy);
  }
</style>
</head>
<body>
<main class="canvas">

  <section class="card card--front" aria-label="Business card front">
    <p class="name">
      <span class="name__line">Rory</span>
      <span class="name__line">Vandermeer</span>
    </p>
    <span class="divider"></span>
    <p class="tagline">Inbound<br>Marketing</p>
  </section>

  <section class="card card--back" aria-label="Business card back">
    <p class="name">
      <span class="name__line">Rory</span>
      <span class="name__line">Vandermeer</span>
    </p>
    <p class="tagline">Inbound Marketing</p>
    <span class="divider"></span>
    <ul class="contact">
      <li class="contact__item">
        <svg class="contact__icon" viewBox="0 0 12 12" aria-hidden="true">
          <path d="M2.5 1 L4.5 1 L5.2 3.6 L3.9 4.6 C4.6 6 6 7.4 7.4 8.1 L8.4 6.8 L11 7.5 L11 9.5 C11 10.4 10.3 11 9.5 11 C5 10.6 1.4 7 1 2.5 C1 1.7 1.6 1 2.5 1 Z" fill="var(--navy)"/>
        </svg>
        512.604.7193
      </li>
      <li class="contact__item">
        <svg class="contact__icon" viewBox="0 0 12 12" aria-hidden="true">
          <rect x="0.5" y="2.5" width="11" height="7.5" fill="var(--navy)"/>
          <path d="M0.8 2.8 L6 6.8 L11.2 2.8" fill="none" stroke="var(--paper)" stroke-width="1"/>
        </svg>
        roryvandermeer@quillmail.net
      </li>
      <li class="contact__item">
        <svg class="contact__icon" viewBox="0 0 12 12" aria-hidden="true" fill="none" stroke="var(--navy)" stroke-width="1">
          <circle cx="6" cy="6" r="5"/>
          <ellipse cx="6" cy="6" rx="2.2" ry="5"/>
          <path d="M1 6 H11 M2 3.5 H10 M2 8.5 H10"/>
        </svg>
        www.roryvandermeer.net
      </li>
    </ul>
    <p class="services">
      Content Strategy<span class="services__sep">|</span>PPC<span class="services__sep">|</span>SEO<span class="services__sep">|</span>Local Social &amp; SEO
    </p>
    <span class="band"></span>
  </section>

</main>
</body>
</html>
```